Bref créative
Real Estate Development Firm
Marlow Holdings
I need double sided standard sized Business Card [3.5" x 2"]
May use same font as in logo or other suggestions
Professional
Derek P. Hollins
President/CEO
248 West Penrose Street
Suite 2360
Milwaukee, WI 53217
dhollins@marlowholdingsllc.example
marlowholdingsllc.example
You can refer to logo design contest for other ideas.
Logo and design or color gradient or other suggestions.
Please use logo

```html
<!DOCTYPE html>
<html lang="en">
<head>
<meta charset="utf-8">
<title>Marlow Holdings – Business Card</title>
<link href="https://fonts.googleapis.com/css2?family=Tinos:wght@400;700&display=swap" rel="stylesheet">
<style>
  :root {
    --page-bg: #ffffff;
    --card-center: #ffffff;
    --card-edge: #d6d6d6;
    --band: #bcbcbc;
    --ink: #111111;
    --brand: #2c3a72;
  }
  html, body {
    margin: 0;
    width: 1200px;
    height: 1011px;
    overflow: hidden;
    background: var(--page-bg);
    font-family: "Tinos", "Times New Roman", serif;
    color: var(--ink);
  }
  .card {
    position: absolute;
    top: 5px;
    width: 574px;
    height: 1001px;
    background: radial-gradient(ellipse at 50% 40%, var(--card-center) 30%, var(--card-edge) 100%);
    overflow: hidden;
  }
  .card--front { left: 8px; }
  .card--back { left: 622px; }
  .card__band {
    position: absolute;
    left: 0; right: 0; bottom: 0;
    height: 38px;
    background: var(--band);
  }
  .holder {
    position: absolute;
    right: 22px;
    top: 22px;
    text-align: right;
  }
  .holder__name {
    font-weight: 700;
    font-size: 34px;
    line-height: 1;
    margin: 0;
  }
  .holder__title {
    font-size: 28px;
    margin: 12px 0 0;
  }
  .brand {
    position: absolute;
    left: 0; right: 0;
    top: 324px;
    text-align: center;
    color: var(--brand);
  }
  .brand__mark {
    display: block;
    margin: 0 auto 80px;
  }
  .brand__name {
    font-size: 56px;
    font-variant: small-caps;
    letter-spacing: 2px;
    line-height: 1;
    margin: 0;
  }
  .brand__tagline {
    font-size: 30px;
    font-variant: small-caps;
    letter-spacing: 2px;
    line-height: 1;
    margin: 10px 0 0;
  }
  .contact {
    position: absolute;
    left: 25px;
    top: 690px;
    font-size: 27px;
    line-height: 33px;
    margin: 0;
    font-style: normal;
  }
</style>
</head>
<body>
  <section class="card card--front">
    <header class="holder">
      <p class="holder__name">Derek P. Hollins</p>
      <p class="holder__title">President/CEO</p>
    </header>
    <div class="brand">
      <svg class="brand__mark" width="80" height="80" viewBox="0 0 80 80" aria-hidden="true">
        <circle cx="40" cy="40" r="40" fill="var(--brand)"/>
      </svg>
      <p class="brand__name">Marlow Holdings</p>
      <p class="brand__tagline">Building Lasting Value</p>
    </div>
    <address class="contact">
      Add : 248 West Penrose Street<br>
      Suite 2360<br>
      Milwaukee, WI 53217<br>
      Ph : 414.555.0100<br>
      Cell : 414.555.0142<br>
      Fax : 414.555.0101<br>
      Email : dhollins@marlowholdingsllc.example<br>
      Web : www.marlowholdingsllc.example
    </address>
    <div class="card__band"></div>
  </section>

  <section class="card card--back">
    <div class="brand">
      <svg class="brand__mark" width="80" height="80" viewBox="0 0 80 80" aria-hidden="true">
        <circle cx="40" cy="40" r="40" fill="var(--brand)"/>
      </svg>
      <p class="brand__name">Marlow Holdings</p>
      <p class="brand__tagline">Building Lasting Value</p>
    </div>
    <div class="card__band"></div>
  </section>
</body>
</html>
```